New Website for Asia Travel Agency

Lanternpath Journeys Website

We want a redesign for our current website, www.lanternpathjourneys.example. We want you to get creative with our brand and present our company in a unique, creative and compelling way, that communicates our exotic destinations and tours, the local and authentic character of our travel consultants and the trustworthy and professional nature of our company.

Who is this company?

Lanternpath Journeys is an online tour operator specializing in providing tailor-made tours to eight destinations in Asia; Vietnam, Thailand, Laos, Cambodia, Indonesia, Myanmar, Japan and China. They were launched in mid February 2012 with headquarters in Bangkok, Thailand, and staffed by locals and expats with many years of experience in the travel industry, and who are committed to sharing their deep knowledge of, and passion for the region.

Local knowledge

Our consultants at Lanternpath Journeys are all locals – they know their destinations inside-out and draw upon invaluable first-hand experience and information when planning your tour. They have insights into local culture and tradition, they know the best places to visit, the most worthwhile experiences to have and, most importantly, they have the knowledge to create exactly the holiday you desire.

All hotels and activities featured in a Lanternpath Journeys tour are regularly inspected by our consultants to ensure the highest quality standards are met and that all information is correct and up to date.

Unforgettable Travel Experiences

Whether it's a cultural exploration or a beach holiday you're after – or a mix of both – Lanternpath Journeys has an itinerary for you – and if we don't have one, we'll tailor-make one! From the main sights to remote villages, our locally based Travel Specialists will give you unique insights into every place you visit and let you delve into known destinations from new perspectives.

Our tours offer a variety of hotel and resort options, premium stays in deluxe accommodation, heritage hotels, a five-star boutique or on the water in a junk. Tap into our experience let us create an experience unique to you – and one you will never forget.

What type of Holiday to Asia?

Our itineraries at Lanternpath Journeys are created according to different inspirations. Some travelers are interested in the History & Culture of a destination, while some like to stay active with Adventure tours. A Cross Border trip explores different countries in a single tour, while Velvet Summit tours offer the highest level of exclusivity across our destinations. There are 14 different Holiday Types to choose from, or you can mix and match ideas to create your dream vacation.

Target Market(s)

Slightly more female, aged 30-65, are creative, professional and looking for something different, something a bit unusual.

Industry/Entity Type

Boutique

Requirements
Must have
• 5 page designs:

1. Homepage
2. Tours list page for a country
3. Tour page
4. 'Be Inspired' page
5. Country page
6. Enquiry page

Our inspirations.

The following list shows websites we love and which inspire us... to give you some indication of our preferred styles, functions and layouts:

http://www.frostmeridian.example/en/ (we really like this, great personality, like the use of icons for tour types)
http://www.pebblewalks.example.uk/ (very simple design elements and layout)
http://www.sunvalecoast.example/ (great use of background image, nice simple nav bar)
http://www.roamcedarfall.example/ (we like because it has distinct personality and is well suited to the destination)
http://www.seemarlowton.example/ (clear personality through font use)
http://www.vastroving.example/ (original, unique)
http://www.wanderquill.example/long-loop-of-asia (like the map style)

Key design points:

1. You must use our existing logo (attached), but you can change the color scheme of the logo to accord with the whichever color scheme you choose for the main designs.
2. Our logo strapline is "Asia is our Lanternpath" and should be used prominently on the page to reinforce the meaning of our company name.
3. Home page and tours list pages should allow the user to see the choice of tours immediately without scrolling & Introduction copy should be minimal.
4. We and our site visitors are inspired and excited by our photography, this is an element of the site which we would like to maintain and build on, though the section page header sliders are currently too big and do not allow quick access to the section content. This is a design problem which needs a solution. Full page photographic backgrounds may be an answer?
5. Tour page should display other contextual tours, from the same country or style/type
6. We should promote press coverage in various places
7. We should display consultant profiles in various places
8. Map designs for tour page and country page, plus a modal pop out for the home page. These are complex and may have a few small photos and short descriptive text only, though this is limited by your own creativity. We will use graphics and html5/css3 so there are no creative limitations.
9. The 'Inspirations' / 'Be Inspired' page is for people who want travel and holiday ideas, who are looking for inspiration on where to go and what to do. This section needs to reflect the exotic, the unusual, the extraordinary in our destinations and tours, and we leave this to your creative genius to develop. We are also interested in how this inspirations page is related to the blog and social media content we produce daily, is there an integration here? Can we present YouTube videos, our blog posts, Facebook posts etc, on this page? This is another design challenge.
10. We would like to see designs for the tours list page which feature AJAX content filtering (for instance: http://demo.layoutbrisk.example/?acn), we would like to see how to include this type of content filtering on homepage and destination page also.
11. The 'Enquiry' call to action should be on all pages and prominent.
12. The enquiry page can reflect the same fields as the existing website enquiry page

Values to be communicated:

- Exotic: Asia is exotic, and our tours will expose clients to extraordinary sights and unusual cultural encounters.
- Authentic: Our travel consultants all live in the destinations themselves, they are local nationals and have all the insider knowledge to give clients a truly authentic experience of our destinations
- Unique: All of our tours are tailor made, there are no fixed departure dates or join-in groups. All tour itineraries can be uniquely designed for our clients, from departure dates to destinations.
- Trust: Some travelers prefer to book their holidays with local agencies they can meet in person, rather than with online companies like us who live in the destinations and who they only get to meet on Skype video or phone. We want to convey that we are trustworthy. We have attempted this through presenting a 'meet the team' page and a 'press' page and advert, as well as offering a prominent international phone number. How we you build on this and further convey this value?

```html
<!DOCTYPE html>
<html lang="en">
<head>
<meta charset="utf-8">
<title>Lanternpath Journeys — Asia is our Lanternpath</title>
<link href="https://fonts.googleapis.com/css2?family=Lato:wght@300;400;700;900&display=swap" rel="stylesheet">
<style>
:root{
  --teal:#1aa88f;
  --orange:#e8821f;
  --ink:#2e2e2e;
  --text:#444;
  --muted:#8a8a8a;
  --paper:#f7f7f5;
  --promo-band:#b9d3d1;
  --footer:#2f2b2b;
  --footer-text:#cfcfcf;
  --white:#fff;
}
*{box-sizing:border-box;margin:0;padding:0}
html,body{width:1200px;height:2510px;overflow:hidden}
body{font-family:'Lato',sans-serif;color:var(--text);background:var(--paper);position:relative}

/* header + hero */
.hero{position:absolute;left:0;top:0;width:1200px;height:716px;
  background:linear-gradient(180deg,#f3dcb4 0%,#f1e6c6 28%,#d9d6a6 48%,#7f8f5a 70%,#3f5a34 100%)}
.logo{position:absolute;left:70px;top:96px;display:flex;align-items:center;gap:10px}
.logo-mark{width:44px;height:44px;background:#a9cfd6;border-radius:6px}
.logo-name{font-weight:900;font-size:20px;color:#333;letter-spacing:-.3px;white-space:nowrap}
.nav-panel{position:absolute;left:360px;top:100px;width:540px;height:60px;background:rgba(255,255,255,.75)}
.nav{position:absolute;left:390px;top:119px;display:flex;gap:26px;font-weight:700;font-size:17px;color:#333;white-space:nowrap}
.nav .active{color:var(--teal)}
.nav .caret{font-size:10px;margin-left:4px}
.search{position:absolute;left:917px;top:118px;width:218px;height:40px;background:var(--teal);color:#e3f6f2;font-size:18px;padding:8px 14px}
.search svg{position:absolute;right:14px;top:10px}
.dots{position:absolute;left:1033px;top:186px;display:flex;gap:13px}
.dots span{width:9px;height:9px;border-radius:50%;background:#fff}
.dots span:first-child{background:var(--teal)}
.hero-title{position:absolute;right:87px;top:390px;font-weight:300;font-size:70px;color:#fff;letter-spacing:-1px;white-space:nowrap}
.btn-peek{position:absolute;left:961px;top:496px;width:152px;height:46px;background:var(--teal);color:#fff;font-weight:700;font-size:19px;text-align:center;line-height:46px}
.choose{position:absolute;left:87px;top:618px;font-size:16px;font-weight:700;letter-spacing:3px;color:#fff}
.dest{position:absolute;top:670px;width:94px;height:94px;border-radius:50%;border:4px solid #fff;transform:translateX(-47px)}
.dest-label{position:absolute;top:773px;width:140px;transform:translateX(-70px);text-align:center;font-size:16px;font-weight:700;color:#999;letter-spacing:.5px}
.dest-label.current{color:#222}

/* why */
.why-title{position:absolute;left:65px;top:868px;font-weight:300;font-size:42px;color:#333}
.why-body{position:absolute;left:65px;top:942px;width:600px;font-size:15.5px;line-height:26px;color:#444}
.why-body p{margin-bottom:22px}
.why-body a{color:#444}
.press{position:absolute;left:765px;top:867px;width:370px;height:380px;background:#fff;border:2px solid #ddd}
.press h3{position:absolute;left:18px;top:18px;font-size:19px;font-weight:400;color:#333}
.press h3 b{font-weight:700}
.press-img{position:absolute;left:40px;top:74px;width:290px;height:200px;border-radius:4px;background:linear-gradient(160deg,#c8c8c8,#8a8078 60%,#5a5a5a)}
.btn-orange{background:var(--orange);color:#fff;font-weight:700;text-align:center;position:absolute}
.press .btn-orange{left:210px;top:325px;width:124px;height:34px;line-height:34px;font-size:16px}

/* promos */
.promos{position:absolute;left:0;top:1317px;width:1200px;height:457px;background:var(--promo-band)}
.promos h2{position:absolute;left:65px;top:34px;font-size:17px;font-weight:700;letter-spacing:4px;color:#333}
.promo-img{position:absolute;top:93px;width:200px;height:200px;border-radius:50%;border:5px solid #fff;transform:translateX(-100px)}
.price{position:absolute;top:252px;width:88px;height:36px;background:#2a2a2a;color:#fff;font-weight:700;font-size:20px;line-height:36px;text-align:center;letter-spacing:1px}
.promo-title{position:absolute;top:308px;width:220px;transform:translateX(-110px);text-align:center;font-weight:700;font-size:16px;line-height:23px;color:#2a2a2a}
.promo-title small{display:block;font-size:13.5px;color:#666}
.promos .btn-orange{top:382px;width:147px;height:37px;line-height:37px;font-size:16px;transform:translateX(-73px)}

/* testimonials */
.quote{position:absolute;top:1840px;width:320px}
.quote-mark{position:absolute;left:-14px;top:-12px;font-family:Georgia,serif;font-size:120px;line-height:1;color:#e4e4e4}
.quote h4{position:relative;font-size:17px;font-weight:700;color:#333;margin-top:26px;line-height:22px}
.quote p{position:relative;font-size:15px;line-height:25px;color:#444}
.quote cite{position:relative;display:block;font-style:normal;font-weight:700;font-size:12.5px;color:var(--orange);margin-top:20px}

/* footer */
.footer{position:absolute;left:0;top:2102px;width:1200px;height:408px;background:var(--footer);color:var(--footer-text)}
.fcol{position:absolute;top:52px}
.fcol h5{font-size:15px;font-weight:700;color:#ddd;margin-bottom:12px;letter-spacing:.5px}
.fcol li{list-style:none;font-size:14px;line-height:19.5px}
.fcol li.current{text-decoration:underline}
.fcol p{font-size:14px;line-height:20px;width:360px}
.footer .btn-orange{left:675px;top:136px;width:124px;height:34px;line-height:34px;font-size:16px}
.social{position:absolute;left:675px;top:247px;display:flex;gap:12px}
.social span{width:34px;height:34px;border-radius:50%;background:#5b5757}
.legal{position:absolute;top:348px;font-size:13.5px}
.skyline{position:absolute;left:612px;top:330px;width:506px;height:78px;background:linear-gradient(180deg,rgba(120,120,120,.15),rgba(120,120,120,.35));border-radius:30px 30px 0 0}
</style>
</head>
<body>

<header class="hero" role="img" aria-label="Misty lakeside temple pavilion at dawn with trees and reeds"></header>
<div class="logo"><span class="logo-mark"></span><span class="logo-name">Lanternpath Journeys</span></div>
<div class="nav-panel"></div>
<nav class="nav">
  <span class="active">Home</span>
  <span>Tours<span class="caret">▼</span></span>
  <span>Holiday Types<span class="caret">▼</span></span>
  <span>Be Inspired</span>
  <span>About Us</span>
</nav>
<div class="search">Search...
  <svg width="20" height="20" viewBox="0 0 20 20"><circle cx="8" cy="8" r="6" fill="none" stroke="#fff" stroke-width="2.5"/><line x1="12.5" y1="12.5" x2="18" y2="18" stroke="#fff" stroke-width="3"/></svg>
</div>
<div class="dots"><span></span><span></span><span></span><span></span><span></span></div>
<h1 class="hero-title">Asia is our Lanternpath.</h1>
<div class="btn-peek">Take a peek</div>

<div class="choose">CHOOSE A DESTINATION</div>
<div class="dest" style="left:132px;background:linear-gradient(#8fb3d4,#4f6f8a)" role="img" aria-label="Thailand temple spires"></div>
<div class="dest" style="left:263px;background:linear-gradient(#a9b0a0,#5f6755)" role="img" aria-label="Indonesia stone stupa"></div>
<div class="dest" style="left:393px;background:linear-gradient(#9fbf8a,#3f6a38)" role="img" aria-label="Laos garden temple"></div>
<div class="dest" style="left:534px;background:linear-gradient(#b4b7b0,#6d6a5e)" role="img" aria-label="Cambodia temple towers"></div>
<div class="dest" style="left:665px;background:linear-gradient(#8fb0d8,#7a3b35)" role="img" aria-label="Japan mountain and pagoda"></div>
<div class="dest" style="left:807px;background:linear-gradient(#b8a58a,#7a5e42)" role="img" aria-label="Myanmar pagoda"></div>
<div class="dest" style="left:941px;background:linear-gradient(#a8c48d,#5d7a42)" role="img" aria-label="Vietnam rice terraces"></div>
<div class="dest" style="left:1071px;background:linear-gradient(#b6c3cf,#6d7a82)" role="img" aria-label="China great wall on hills"></div>
<div class="dest-label" style="left:132px">THAILAND</div>
<div class="dest-label" style="left:263px">INDONESIA</div>
<div class="dest-label" style="left:393px">LAOS</div>
<div class="dest-label" style="left:534px">CAMBODIA</div>
<div class="dest-label current" style="left:665px">JAPAN</div>
<div class="dest-label" style="left:807px">MYANMAR</div>
<div class="dest-label" style="left:941px">VIETNAM</div>
<div class="dest-label" style="left:1071px">CHINA</div>

<section>
  <h2 class="why-title">Why Lanternpath Journeys ?</h2>
  <div class="why-body">
    <p>No one knows a destination better than someone who lives, works and plays there. That's the foundation of Lanternpath Journeys.<br>Our travel specialists reside in Asia. They live Asia, they breathe Asia. And they're intrigued explorers as much as they are citizens of Bangkok, or Bali, or Luang Prabang.</p>
    <p>The result is a travel company tailor-made for the person with a taste for veering off the well-trodden path, for the adventurer who wants access to Asia's most spectacular sights, but hidden charms as well, on the road less traveled.</p>
    <p>Want to explore this Asia? <a href="#">Step into our Lanternpath.</a></p>
  </div>
  <aside class="press">
    <h3>OUR LATEST <b>PRESS COVERAGE</b></h3>
    <div class="press-img" role="img" aria-label="Stack of travel magazines"></div>
    <div class="btn-orange">MORE INFO</div>
  </aside>
</section>

<section class="promos">
  <h2>FEATURED PROMOTIONS</h2>
  <div class="promo-img" style="left:169px;background:linear-gradient(135deg,#8cc04a,#3f7a22)" role="img" aria-label="Green tea terraces"></div>
  <div class="promo-img" style="left:457px;background:linear-gradient(180deg,#9fb4c4,#8a5a3a)" role="img" aria-label="Ancient pagodas on a plain"></div>
  <div class="promo-img" style="left:742px;background:linear-gradient(180deg,#b5885a,#6a3c22)" role="img" aria-label="Traditional dancer in golden headdress"></div>
  <div class="promo-img" style="left:1031px;background:linear-gradient(180deg,#c9c0a8,#5b4a3a)" role="img" aria-label="Road sign warning of elephants"></div>
  <div class="price" style="left:84px">$1153</div>
  <div class="price" style="left:372px">$624</div>
  <div class="price" style="left:656px">$315</div>
  <div class="price" style="left:946px">$424</div>
  <div class="promo-title" style="left:169px">A JAVANESE JOURNEY<small>7 DAYS / 6 NIGHTS</small></div>
  <div class="promo-title" style="left:457px;top:297px">A TALE OF TWO CITIES:<br>MANDALAY TO BAGAN<small>4 DAYS / 3 NIGHTS</small></div>
  <div class="promo-title" style="left:742px;top:297px">ANCIENT EMPIRE:<br>EXPLORE ANGKOR<small>4 DAYS / 3 NIGHTS</small></div>
  <div class="promo-title" style="left:1031px;top:297px">ANGKOR WAT FAMILY<br>ADVENTURE<small>4 DAYS / 3 NIGHTS</small></div>
  <div class="btn-orange" style="left:169px">Send an inquiry</div>
  <div class="btn-orange" style="left:457px">Send an inquiry</div>
  <div class="btn-orange" style="left:742px">Send an inquiry</div>
  <div class="btn-orange" style="left:1031px">Send an inquiry</div>
</section>

<section>
  <blockquote class="quote" style="left:79px">
    <span class="quote-mark">“</span>
    <h4>GREAT SUCCESS</h4>
    <p>It was a terrific trip and we are most grateful for the careful attention you gave all our requests.</p>
    <cite>MR. HARLAN EVERETT QUINCE</cite>
  </blockquote>
  <blockquote class="quote" style="left:450px">
    <span class="quote-mark">“</span>
    <h4>AN ITINERARY JUST RIGHT</h4>
    <p>We had a great trip. Thank you so much for all the preparation work to get the itinerary just right.</p>
    <cite>TAMSIN ARVALE</cite>
  </blockquote>
  <blockquote class="quote" style="left:825px;width:290px">
    <span class="quote-mark">“</span>
    <h4>AMAZING JOURNEY,<br>THANKS SO MUCH</h4>
    <p>Back now and still recovering from our amazing journey. It was a fantastic trip.</p>
    <cite>MRS. ODETTE R. FENWICK</cite>
  </blockquote>
</section>

<footer class="footer">
  <div class="fcol" style="left:65px"><h5>QUICK LINKS</h5><ul>
    <li class="current">Home</li><li>Destinations</li><li>Tours</li><li>Holiday Types</li><li>Best Value</li><li>About Us</li><li>Blog</li></ul></div>
  <div class="fcol" style="left:240px"><h5>OUR LANTERNPATH</h5><ul>
    <li>Thailand</li><li>Indonesia</li><li>Laos</li><li>Cambodia</li><li>Japan</li><li>Myanmar</li><li>Vietnam</li><li>China</li><li>Multi-Country</li></ul></div>
  <div class="fcol" style="left:435px"><h5>ABOUT US</h5><ul>
    <li>Why Book With Us</li><li>About Us</li><li>Meet The Team</li><li>Careers</li><li>In The Press</li><li>Affiliate Program</li></ul></div>
  <div class="fcol" style="left:675px"><h5>SUBSCRIBE TO OUR E-NEWSLETTER</h5>
    <p>Sign up for Lanternpath Journeys's e-newsletter featuring promotions, travel musings and insider destination.</p></div>
  <div class="btn-orange">SUBSCRIBE</div>
  <div class="fcol" style="left:675px;top:212px"><h5>FOLLOW US</h5></div>
  <div class="social"><span></span><span></span><span></span><span></span></div>
  <div class="skyline" role="img" aria-label="Faint silhouette of Asian landmarks"></div>
  <div class="legal" style="left:65px">Contact Us | Terms</div>
  <div class="legal" style="left:240px">© 2013 Lanternpath Journeys. All Rights Reserved</div>
</footer>

</body>
</html>
```